MSA Plans

I would like to rebuild my brochure for the 3 business plans that I currently offer my clients. I would like to make it look much more modern & attractive to clients when choosing one of our service plans. If we can stick to a tech theme that would be great. Message me for anymore information.

```html
<!DOCTYPE html>
<html lang="en">
<head>
<meta charset="utf-8">
<title>Managed Services Framework – Bytewell</title>
<link rel="stylesheet" href="https://fonts.googleapis.com/css2?family=Barlow+Condensed:wght@500;600&family=Montserrat:wght@500;600;700&family=Barlow:wght@400;600&display=swap">
<style>
  :root{
    --stage:#808080;
    --paper:#f7f7f7;
    --orange:#f26522;
    --orange-soft:#f7a06c;
    --ink:#1c1c1c;
    --muted:#555;
    --rule:#9a9a9a;
    --tick:#3a9a2a;
    --cross:#e02020;
    --tab:#111;
    --swoosh:#c9c9c9;
  }
  *{box-sizing:border-box;margin:0;padding:0}
  html,body{width:1200px;height:1200px;overflow:hidden;background:var(--stage)}
  .page{position:absolute;left:475px;width:250px;height:350px;background:var(--paper);overflow:hidden;font-family:'Montserrat',sans-serif;color:var(--ink)}
  .page--cover{top:56px}
  .page--plans{top:426px}
  .page--security{top:799px}

  .brand{position:absolute;top:13px;left:0;width:100%;display:flex;justify-content:center;align-items:center;gap:4px;font-family:'Montserrat',sans-serif;font-weight:700;font-size:10px;color:var(--orange);letter-spacing:.5px}
  .brand__mark{width:9px;height:9px;background:var(--orange)}
  .cover-title{position:absolute;right:12px;top:44px;text-align:right;font-family:'Barlow Condensed',sans-serif;font-weight:500;font-size:17px;line-height:16.5px;color:var(--orange)}
  .cover-art{position:absolute;left:0;top:0;width:250px;height:260px}
  .cover-meta{position:absolute;top:262px;width:100%;text-align:center;font-size:4.8px;line-height:13px}
  .cover-meta .accent{color:var(--orange);font-weight:600}

  .footer{position:absolute;left:0;bottom:0;width:250px;height:45px}
  .footer svg{position:absolute;left:0;top:0}
  .footer__text{position:absolute;left:0;bottom:6px;width:100%;text-align:center;font-size:4.2px;line-height:6px;font-weight:500}
  .footer__company{color:var(--orange);font-weight:700}

  .top-photo{position:absolute;left:0;top:0;width:250px;height:72px;background:linear-gradient(180deg,#b9bfc6 0%,#dde1e5 60%,var(--paper) 100%);opacity:.85}
  .bottom-photo{position:absolute;left:0;top:182px;width:250px;height:168px;background:radial-gradient(ellipse at 50% 45%,#c9a48c 0%,#8fa3b3 40%,#5c7385 75%,#33495a 100%)}

  .plan-table{position:absolute;left:22px;width:213px;border-collapse:collapse;font-family:'Barlow',sans-serif;font-size:3.4px;table-layout:fixed}
  .plan-table th{background:var(--orange);color:#fff;font-weight:600;height:15px;font-size:3.6px}
  .plan-table th.plan-table__title{font-family:'Montserrat',sans-serif;font-size:4.2px;text-align:center;border-top-left-radius:6px}
  .plan-table th:last-child{border-top-right-radius:6px}
  .plan-table th+th{border-left:.5px solid #fff}
  .plan-table td{height:8.45px;border-bottom:.5px solid var(--rule);text-align:center;background:#fff}
  .plan-table td:first-child{text-align:left;padding-left:7px}
  .plan-table td+td{border-left:.5px solid var(--rule)}
  .tick{color:var(--tick);font-size:5px;font-weight:600}
  .cross{color:var(--cross);font-size:4.5px;font-weight:700}
  .price td{color:var(--orange);font-weight:600}
  .strong td:first-child{font-weight:600}

  .side-tab{position:absolute;left:10px;width:11px;background:var(--tab);border-radius:5px 0 0 5px;display:flex;align-items:center;justify-content:center}
  .side-tab span{transform:rotate(-90deg);white-space:nowrap;color:var(--orange);font-size:3.8px;font-weight:700;font-family:'Barlow',sans-serif}
</style>
</head>
<body>

<!-- Cover page -->
<section class="page page--cover">
  <svg class="cover-art" viewBox="0 0 250 260">
    <path d="M0 20 C70 40 170 80 230 170 C245 200 240 220 200 228 C140 240 60 228 0 212 Z" fill="#f3d8c8"/>
    <path d="M0 212 C60 228 140 240 200 228 C240 220 250 190 250 150 L250 190 C245 240 160 262 90 250 C50 244 20 236 0 232 Z" fill="var(--orange)" opacity=".9"/>
    <path d="M0 20 C70 40 170 80 230 170 C238 186 236 196 228 200 C220 150 130 70 0 40 Z" fill="#ffffff"/>
    <g role="img" aria-label="Photo of a technician working on computer hardware at a desk">
      <path d="M0 42 C120 70 210 140 226 196 C232 216 200 222 150 222 C90 222 40 214 0 206 Z" fill="url(#coverPhoto)"/>
    </g>
    <defs>
      <linearGradient id="coverPhoto" x1="0" y1="0" x2="1" y2="1">
        <stop offset="0" stop-color="#8a6a55"/>
        <stop offset=".45" stop-color="#9aa9b6"/>
        <stop offset="1" stop-color="#3c3f44"/>
      </linearGradient>
    </defs>
  </svg>
  <div class="brand"><span class="brand__mark"></span>BYTEWELL</div>
  <h1 class="cover-title">Managed Services<br>Framework</h1>
  <div class="cover-meta">
    <p>Version 1.0</p>
    <p><span class="accent">Updated:</span> April 2024</p>
    <p>Defining our services and how we deliver these consistently to you.</p>
  </div>
  <div class="footer">
    <svg width="250" height="45" viewBox="0 0 250 45"><path d="M0 45 C20 10 120 -2 250 20 L250 24 C130 6 30 16 8 45 Z" fill="var(--swoosh)"/><path d="M0 30 C10 20 30 14 60 10 C30 18 10 28 4 45 L0 45 Z" fill="#999"/></svg>
    <div class="footer__text">
      <p class="footer__company">BYTEWELL COMPUTER SERVICES PTY LTD</p>
      <p>bytewellcomputers.com.au | service@bytewellcomputers.com.au</p>
      <p>12/40 Sample St, Northvale, VIC, 3000 | 1300 000 111 | ABN: 00 000 000 000</p>
    </div>
  </div>
</section>

<!-- Plans page -->
<section class="page page--plans">
  <div class="top-photo" role="img" aria-label="Faded photo of people working at laptops with technology icons overlaid"></div>
  <div class="side-tab" style="top:83px;height:34px"><span>Support</span></div>
  <div class="side-tab" style="top:119px;height:34px"><span>Service</span></div>
  <div class="side-tab" style="top:203px;height:35px"><span>Management</span></div>
  <div class="side-tab" style="top:249px;height:35px"><span>Training</span></div>
  <table class="plan-table" style="top:68px">
    <colgroup><col style="width:132px"><col><col><col></colgroup>
    <thead><tr><th class="plan-table__title">Managed Services Agreement</th><th>Essential</th><th>Business</th><th>Professional</th></tr></thead>
    <tbody>
      <tr><td>Unlimited Remote Support 7am to 6pm</td><td class="tick">✓</td><td class="tick">✓</td><td class="tick">✓</td></tr>
      <tr><td>3rd Party Vendor Support</td><td class="tick">✓</td><td class="tick">✓</td><td class="tick">✓</td></tr>
      <tr><td>Reactive Onsite Support 8am to 5pm</td><td>VIP Rates</td><td class="tick">✓</td><td class="tick">✓</td></tr>
      <tr><td>After-Hours Support</td><td>VIP Rates</td><td>VIP Rates</td><td class="tick">✓</td></tr>
      <tr><td>Guaranteed SLA Response Times</td><td class="tick">✓</td><td class="tick">✓</td><td class="tick">✓</td></tr>
      <tr><td>24x7 Website &amp; Infrastructure Monitoring</td><td class="tick">✓</td><td class="tick">✓</td><td class="tick">✓</td></tr>
      <tr><td>Secure Web Content Filtering</td><td class="tick">✓</td><td class="tick">✓</td><td class="tick">✓</td></tr>
      <tr><td>Backup Monitoring</td><td class="tick">✓</td><td class="tick">✓</td><td class="tick">✓</td></tr>
      <tr><td>Desktop OS Patching &amp; Updating</td><td class="tick">✓</td><td class="tick">✓</td><td class="tick">✓</td></tr>
      <tr><td>CEO / MD Home Tech Support</td><td class="tick">✓</td><td class="tick">✓</td><td class="tick">✓</td></tr>
      <tr><td>Monthly Tech Site Visit</td><td class="cross">✕</td><td>Quarterly</td><td>Monthly</td></tr>
      <tr><td>Short Term Loan Equipment</td><td class="cross">✕</td><td>1 Month</td><td>3 Months</td></tr>
      <tr><td>Adds / Moves / Changes (Staff)</td><td class="tick">✓</td><td class="tick">✓</td><td class="tick">✓</td></tr>
      <tr><td>Adds / Moves / Changes (Workstations)</td><td>VIP Rates</td><td>VIP Rates</td><td class="tick">✓</td></tr>
      <tr><td>Asset and Warranty Tracking &amp; Reporting</td><td class="tick">✓</td><td class="tick">✓</td><td class="tick">✓</td></tr>
      <tr><td>Comprehensive IT Documentation</td><td class="tick">✓</td><td class="tick">✓</td><td class="tick">✓</td></tr>
      <tr><td>Technology Strategy Meeting</td><td>Annual</td><td>Quarterly</td><td>Monthly</td></tr>
      <tr><td>Technology Business Review Meeting</td><td>Annual</td><td>Bi Annual</td><td>Quarterly</td></tr>
      <tr><td>IT Policy Templates</td><td class="cross">✕</td><td class="tick">✓</td><td class="tick">✓</td></tr>
      <tr><td>End User Training Materials</td><td class="cross">✕</td><td class="cross">✕</td><td class="tick">✓</td></tr>
      <tr><td>Security Awareness Training</td><td class="tick">✓</td><td class="tick">✓</td><td class="tick">✓</td></tr>
      <tr class="price"><td>RRP / User</td><td>$110</td><td>$130</td><td>$165</td></tr>
      <tr class="price"><td>Minimum User Count</td><td>5</td><td>5</td><td>5</td></tr>
      <tr class="price"><td>Minimum Monthly Commit</td><td>$550</td><td>$650</td><td>$825</td></tr>
    </tbody>
  </table>
  <div class="footer">
    <svg width="250" height="45" viewBox="0 0 250 45"><path d="M0 45 C20 10 120 -2 250 20 L250 24 C130 6 30 16 8 45 Z" fill="var(--swoosh)"/><path d="M0 30 C10 20 30 14 60 10 C30 18 10 28 4 45 L0 45 Z" fill="#999"/></svg>
    <div class="footer__text">
      <p class="footer__company">BYTEWELL COMPUTER SERVICES PTY LTD</p>
      <p>bytewellcomputers.com.au | service@bytewellcomputers.com.au</p>
      <p>12/40 Sample St, Northvale, VIC, 3000 | 1300 000 111 | ABN: 00 000 000 000</p>
    </div>
  </div>
</section>

<!-- Security add-on page -->
<section class="page page--security">
  <div class="bottom-photo" role="img" aria-label="Photo of a smiling woman working on a laptop with network graphics overlaid"></div>
  <div class="side-tab" style="top:34px;height:35px"><span>Support</span></div>
  <table class="plan-table" style="top:18px">
    <colgroup><col style="width:159px"><col><col></colgroup>
    <thead><tr><th class="plan-table__title"></th><th>Business</th><th>Professional</th></tr></thead>
    <tbody>
      <tr><td>Compliance with National Baseline 8 Maturity</td><td class="tick">✓</td><td class="tick">✓</td></tr>
      <tr><td>Security Standard – Alignment to Bytewell Cloud Suite Security Policy &amp; Reporting</td><td class="tick">✓</td><td class="tick">✓</td></tr>
      <tr><td>24x7 Security Operations Centre (SOC) – Monitoring Cloud Suite</td><td class="tick">✓</td><td class="tick">✓</td></tr>
      <tr><td>Dark Web Scanning</td><td class="tick">✓</td><td class="tick">✓</td></tr>
      <tr><td>Cloud Email Filtering</td><td class="tick">✓</td><td class="tick">✓</td></tr>
      <tr><td>Cloud Suite Backup</td><td class="tick">✓</td><td class="tick">✓</td></tr>
      <tr><td>Automated Email Signatures</td><td class="tick">✓</td><td class="tick">✓</td></tr>
      <tr><td>Endpoint Protection with EDR – Workstations &amp; Servers</td><td class="tick">✓</td><td class="tick">✓</td></tr>
      <tr><td>3rd Party Applications Updating</td><td class="cross">✕</td><td class="tick">✓</td></tr>
      <tr><td>24x7 Security Operations Centre (SOC) – Monitoring Endpoints and Servers</td><td class="cross">✕</td><td class="tick">✓</td></tr>
      <tr><td>Privileged Access Management &amp; Application Whitelisting</td><td class="cross">✕</td><td class="tick">✓</td></tr>
      <tr><td>Internal Vulnerability Scanning</td><td class="cross">✕</td><td class="tick">✓</td></tr>
      <tr><td style="height:13px">Backup &amp; Disaster Recovery to comply with National Baseline 8 Maturity Level 1</td><td class="cross">✕</td><td>Pending<br>Assessment</td></tr>
      <tr class="price"><td>RRP / User</td><td>$35</td><td>$60</td></tr>
      <tr class="price strong"><td style="color:var(--ink)">Minimum User Count</td><td>5</td><td>5</td></tr>
      <tr class="price strong"><td style="color:var(--ink)">Minimum Monthly Commit</td><td>$175</td><td>$30</td></tr>
    </tbody>
  </table>
  <div class="footer">
    <svg width="250" height="45" viewBox="0 0 250 45"><path d="M0 45 C30 18 120 10 250 22 L250 45 Z" fill="#fff"/></svg>
    <div class="footer__text">
      <p class="footer__company">BYTEWELL COMPUTER SERVICES PTY LTD</p>
      <p>bytewellcomputers.com.au | service@bytewellcomputers.com.au</p>
      <p>12/40 Sample St, Northvale, VIC, 3000 | 1300 000 111 | ABN: 00 000 000 000</p>
    </div>
  </div>
</section>

</body>
</html>
```